Design a DL flyer double sided 4 colour 210mm x 95 mm (portrait) for the launch of a new yoga studio opening in North Melbourne on the 23 November 2013.
The final design should communicate with a strong call to action- the opening date , register to receive your first class free and like us on Chatterbox.
The studio provides a tranquil, open space to practice yoga, create a feeling of light, peace and a nurturing environment, please create this feeling in the design.

An example design mock (rough design feel free to move around as required, includes final content) print specifications, logo, typography style and image attached.
The reverse side to include logo, address and please design the timetable for the launch week (refer design mock)
Have also attached a reverse logo for a dark background and are open to designer providing examples with various background colours and effects.
Back content can be moved to the front side if required to facilitate design

Target Market(s)

People in the area who are practicing yoga elsewhere and encourage them to come to the studio to try us out with a free opening offer in our first week. And people new to yoga wanting to give it a try.
Experienced yoga people and people new to yoga - all ages

Industry/Entity Type

Environment

Requirements
Must have
• The Lotus Nook logo physical address, website address, the tagline live, breathe, love...
The final design should communicate with a strong call to action- the opening date , register to receive your first class free and like us on Chatterbox. and the website address thelotusnook.com.au, drive them to the website to register.
The studio provides a tranquil, open space to practice yoga, create a feeling of light, peace and a nurturing environment, please create this feeling in the design

```html
<!DOCTYPE html>
<html lang="en">
<head>
<meta charset="utf-8">
<title>The Lotus Nook – Opening Flyer</title>
<link href="https://fonts.googleapis.com/css2?family=PT+Sans+Narrow:wght@400;700&display=swap" rel="stylesheet">
<style>
:root{
  --orange:#f7941d;
  --orange-deep:#e8782a;
  --orange-light:#f5b24c;
  --charcoal:#333333;
  --ink:#3a3a3a;
  --paper:#ffffff;
  --stage-top:#ffffff;
  --stage-bottom:#a9a9a9;
  --leaf:#5f7a4a;
  --leaf-light:#c9d4bc;
  --map:#e9e4da;
}
*{margin:0;padding:0;box-sizing:border-box}
html,body{width:1200px;height:748px;overflow:hidden}
body{
  position:relative;
  font-family:"PT Sans Narrow","Arial Narrow",sans-serif;
  background:linear-gradient(180deg,var(--stage-top) 0%,#eeeeee 35%,var(--stage-bottom) 100%);
  color:var(--ink);
}
.abs{position:absolute}

/* ---------- Front side ---------- */
.front{
  left:26px;top:24px;width:330px;height:700px;
  background:var(--paper);
  box-shadow:4px 6px 10px rgba(0,0,0,.35);
  overflow:hidden;
}
.brand{left:30px;top:22px;display:flex;align-items:center;gap:6px}
.brand-dot{width:22px;height:22px;border-radius:50%;background:var(--orange)}
.brand-name{font-size:22px;font-weight:700;color:var(--orange);letter-spacing:-.3px}
.tagline{left:66px;top:56px;font-size:14px;font-weight:700;color:var(--orange)}
.headline{left:0;width:100%;top:90px;text-align:center;font-size:38px;font-weight:700;color:var(--orange);line-height:1}
.opening{left:0;width:100%;top:130px;text-align:center;padding-left:50px;font-size:22px;font-weight:700;color:var(--charcoal)}
.opening span{color:var(--orange)}
.offer{
  left:72px;top:186px;width:176px;height:100px;
  background:var(--charcoal);
  transform:rotate(-8deg);
  box-shadow:2px 3px 6px rgba(0,0,0,.3);
  text-align:center;padding-top:10px;line-height:1;
}
.offer-title{font-size:27px;font-weight:700;color:var(--orange)}
.offer-sub{font-size:21px;font-weight:700;color:var(--orange);margin-top:2px}
.offer-dates{font-size:23px;font-weight:700;color:var(--paper);margin-top:7px}
.cta{left:0;width:100%;top:320px;text-align:center;font-size:17px;font-weight:700;color:var(--ink);line-height:23px}
.cta em{font-style:normal;color:var(--orange)}
.scene{
  left:0;top:368px;width:330px;height:290px;
  background:linear-gradient(180deg,var(--paper) 0%,var(--leaf-light) 20%,var(--leaf) 60%,#3e5234 100%);
}
.front-foot{left:0;top:656px;width:330px;height:44px;background:var(--charcoal);display:flex;align-items:center;padding-left:30px;gap:10px}
.front-foot span{font-size:16px;font-weight:700;color:var(--orange);white-space:nowrap}

/* ---------- Back side ---------- */
.back{
  left:373px;top:186px;width:798px;height:375px;
  background:linear-gradient(180deg,#f7f7f7,var(--paper) 40%);
  box-shadow:4px 6px 10px rgba(0,0,0,.35);
  overflow:hidden;
}
.back-mark{left:66px;top:40px;width:66px;height:66px;border-radius:50%;background:var(--orange)}
.intro{left:140px;top:44px;width:608px;text-align:center;font-size:16.5px;color:var(--orange);line-height:23px}
.intro-lead{color:var(--ink)}
.intro-lead b{color:var(--orange)}
.timetable-panel{
  left:0;top:124px;width:515px;height:168px;
  background:linear-gradient(180deg,var(--orange-light),var(--orange-deep));
}
.timetable-title{left:44px;top:6px;font-size:21px;font-weight:700;color:var(--paper)}
.timetable{left:45px;top:35px;width:428px;border-collapse:collapse;font-size:15px;font-weight:700;color:var(--paper)}
.timetable th{background:var(--paper);color:var(--orange-deep);text-align:left;padding:0 4px;height:18px;font-weight:700}
.timetable td{padding:0 4px;height:21px;white-space:nowrap}
.map{left:523px;top:124px;width:275px;height:168px;background:linear-gradient(135deg,var(--map),#d8d2c4)}
.map-tag{left:572px;top:278px;width:155px;height:26px;background:var(--orange);color:var(--charcoal);font-size:17px;font-weight:700;text-align:center;line-height:26px;z-index:2;white-space:nowrap}
.back-foot{left:0;top:292px;width:798px;height:83px;background:var(--charcoal);z-index:1}
.social-box{left:42px;top:17px;width:43px;height:43px;border:2px solid var(--orange);border-radius:5px;background:#4a4a4a}
.social{left:90px;top:29px;font-size:16.5px;font-weight:700;color:var(--orange);white-space:nowrap;letter-spacing:-.2px}
.social b{color:var(--paper)}
.divider{left:416px;top:12px;width:2px;height:56px;background:var(--orange)}
.address{left:424px;top:18px;width:154px;text-align:center;font-size:16px;color:var(--paper);line-height:23px;white-space:nowrap}
.contact{left:582px;top:16px;width:170px;text-align:center;color:var(--orange);font-size:16px;line-height:20px;white-space:nowrap}
.contact .phone{font-size:21px;line-height:26px}
</style>
</head>
<body>

<section class="front abs">
  <div class="brand abs"><div class="brand-dot"></div><div class="brand-name">The Lotus Nook</div></div>
  <div class="tagline abs">live, breathe, love...</div>
  <h1 class="headline abs">New Yoga Studio</h1>
  <div class="opening abs">opening <span>23 November</span></div>
  <div class="offer abs">
    <div class="offer-title">First class free</div>
    <div class="offer-sub">in opening week</div>
    <div class="offer-dates">23 Nov – 29 Nov</div>
  </div>
  <p class="cta abs">To <em>book your free class</em><br>go to <em>thelotusnook.com.au</em> to register.</p>
  <div class="scene abs" role="img" aria-label="Photo of a woman meditating cross-legged beside still water in a lush green forest"></div>
  <div class="front-foot abs">
    <svg width="16" height="24" viewBox="0 0 16 24" aria-hidden="true"><path d="M8 0a8 8 0 0 0-8 8c0 6 8 16 8 16s8-10 8-16a8 8 0 0 0-8-8z" fill="#f7941d"/><circle cx="8" cy="8" r="3" fill="#333"/></svg>
    <span>48 ASHGROVE STREET, NORTH MELBOURNE</span>
  </div>
</section>

<section class="back abs">
  <div class="back-mark abs" aria-hidden="true"></div>
  <div class="intro abs">
    A generously sized dedicated yoga studio in North Melbourne, providing dynamic flow vinyasa and<br>
    restorative yoga for all levels from newbies to experienced, with a collection of the best teachers.<br>
    <span class="intro-lead">Embark on a journey to happiness within yourself, <b>be healthy in your body and mind.</b></span>
  </div>

  <div class="timetable-panel abs">
    <div class="timetable-title abs">Class Times</div>
    <table class="timetable abs">
      <tr><th>Sat</th><th>Sun</th><th>Mon</th><th>Tue</th><th>Wed</th><th>Thu</th><th>Fri</th></tr>
      <tr><td>9:00 AM</td><td>9:00 AM</td><td>6.30AM</td><td>6.30AM</td><td>6.30AM</td><td>6.30AM</td><td>6.30AM</td></tr>
      <tr><td>10.30 AM</td><td>10.30 AM</td><td>9.30AM</td><td>9.30AM</td><td>9.30AM</td><td>9.30AM</td><td>9.30AM</td></tr>
      <tr><td>4PM</td><td>4PM</td><td>12.30PM</td><td>12.30PM</td><td>12.30PM</td><td>12.30PM</td><td>12.30PM</td></tr>
      <tr><td></td><td></td><td>5.30PM</td><td>5.30PM</td><td>5.30PM</td><td>5.30PM</td><td>5.30PM</td></tr>
      <tr><td></td><td></td><td>7PM</td><td>7PM</td><td>7PM</td><td>7PM</td><td>7PM</td></tr>
    </table>
  </div>

  <div class="map abs" role="img" aria-label="Street map of North Melbourne marking the studio location"></div>

  <div class="back-foot abs">
    <div class="social-box abs" aria-hidden="true"></div>
    <div class="social abs">like us on Chatterbox @ <b>The Lotus Nook-Melbourne</b></div>
    <div class="divider abs"></div>
    <div class="address abs">48 Ashgrove Street<br>North Melbourne VIC 3003</div>
    <div class="contact abs">hello@thelotusnook.com.au<br><span class="phone">0400 555 018</span></div>
  </div>

  <div class="map-tag abs">thelotusnook.com.au</div>
</section>

</body>
</html>
```